modern, IT themed business card for IT accelerator

Design a business card for tech oriented business accelerator. Prevailing color shall be orange.
we are operating in emerging markets and our mission is to provide co-working space, mentorship/coaching and ultimately seed financing IT startups.
also, we are helping financed ITs in obtaining next round financing, and to this end we are meeting with non IT/finance people and investment professionals..
that means card shall be designed to "impress" not only IT people (mostly liberal) but finance (more conservative)

Industry/Entity Type

Investment

Contact Information for Business Card

Company Name: Pelor Founders Yard
Name: Temur Kobaladze
Position: Partner
Address: 14, N Abashidze St., Tbilisi 0162, Georgia
Tel: +995599438165
Email: t.kobaladze@pelorhub.ge
Website: www.pelorhub.ge

Font styles to use
Sans Serif

Requirements
Must have
• Attached are logos of the company (portrait & landscape) choose any
Nice to have
• industry is IT and finance (in fact, financing IT startups). therefore design might have IT theme (inspiration from web or software designs)

```html
<!DOCTYPE html>
<html lang="en">
<head>
<meta charset="utf-8">
<title>Pelor Founders Yard – Business Card</title>
<link href="https://fonts.googleapis.com/css2?family=Fira+Sans:wght@400;600;700&display=swap" rel="stylesheet">
<style>
  :root {
    --backdrop: #ececec;
    --paper: #fbfbfb;
    --orange-light: #e4a66e;
    --orange-deep: #d7873c;
    --ink-grey: #7b7b7b;
    --ink-light: #f6f1ea;
    --bulb-fill: #f2f2f2;
  }
  * { margin: 0; padding: 0; box-sizing: border-box; }
  html, body {
    width: 1200px; height: 720px; overflow: hidden;
    background: var(--backdrop);
    font-family: "Fira Sans", Arial, sans-serif;
  }
  .canvas {
    position: relative; width: 1200px; height: 720px;
    display: flex; align-items: center; justify-content: center; gap: 60px;
  }
  .card {
    width: 510px; height: 292px; position: relative; overflow: hidden;
    box-shadow: 0 6px 18px rgba(0,0,0,0.12);
  }
  .card--front {
    background: var(--paper);
    display: flex; flex-direction: column; align-items: center; justify-content: center; gap: 18px;
  }
  .brand-mark {
    width: 96px; height: 96px; border-radius: 50%;
    background: var(--bulb-fill); border: 3px solid var(--ink-grey);
  }
  .brand-name {
    color: var(--ink-grey); font-weight: 600; font-size: 30px; letter-spacing: 1px;
    text-transform: uppercase; text-align: center; line-height: 1.1;
  }
  .card--back {
    background: linear-gradient(160deg, var(--orange-light), var(--orange-deep));
  }
  .back-brand {
    position: absolute; left: 28px; top: 60px; width: 160px;
    display: flex; flex-direction: column; align-items: center; gap: 14px;
  }
  .back-brand .brand-mark { width: 110px; height: 110px; }
  .back-brand .brand-name { font-size: 20px; }
  .contact {
    position: absolute; left: 220px; top: 30px; right: 24px;
    color: var(--ink-grey);
  }
  .contact__name {
    color: var(--ink-light); font-weight: 700; font-size: 24px; letter-spacing: 1px;
    text-transform: uppercase;
  }
  .contact__role { font-style: italic; font-size: 17px; margin: 2px 0 0 30px; }
  .contact__address { font-size: 17px; line-height: 1.3; margin: 22px 0 0 90px; }
  .contact__lines { list-style: none; margin: 16px 0 0 30px; font-size: 17px; line-height: 1.45; }
  .contact__lines li { display: flex; align-items: center; gap: 10px; }
  .contact__lines svg { width: 15px; height: 15px; flex: none; }
</style>
</head>
<body>
<main class="canvas">
  <section class="card card--front">
    <div class="brand-mark" aria-hidden="true"></div>
    <div class="brand-name">Pelor Founders Yard</div>
  </section>

  <section class="card card--back">
    <div class="back-brand">
      <div class="brand-mark" aria-hidden="true"></div>
      <div class="brand-name">Pelor Founders Yard</div>
    </div>
    <div class="contact">
      <h1 class="contact__name">Temur Kobaladze</h1>
      <p class="contact__role">Partner</p>
      <p class="contact__address">14, N Abashidze St.,<br>Tbilisi 0162,<br>Georgia</p>
      <ul class="contact__lines">
        <li>
          <svg viewBox="0 0 16 16" fill="none" stroke="#f6f1ea" stroke-width="1.4"><circle cx="8" cy="8" r="7"/><path d="M5.5 4.5l1.5 1.5-1 1c.6 1.3 1.5 2.2 2.8 2.8l1-1 1.5 1.5-1 1c-2.7-.4-5.3-3-5.8-5.8z" fill="#f6f1ea"/></svg>
          +995599438165
        </li>
        <li>
          <svg viewBox="0 0 16 16" fill="none" stroke="#f6f1ea" stroke-width="1.4"><rect x="1.5" y="3.5" width="13" height="9"/><path d="M1.5 3.5l6.5 5 6.5-5"/></svg>
          t.kobaladze@pelorhub.ge
        </li>
        <li>
          <svg viewBox="0 0 16 16" fill="none" stroke="#f6f1ea" stroke-width="1.4"><circle cx="8" cy="8" r="6.5"/><ellipse cx="8" cy="8" rx="3" ry="6.5"/><path d="M1.5 8h13"/></svg>
          www.pelorhub.ge
        </li>
      </ul>
    </div>
  </section>
</main>
</body>
</html>
```